Italian restaurant needs new site

Need to make our website better.

Must have reservation module

Must be able to sell wine tasting tours and wine pairing tours and intégrate with lumo desk

Blog

Social media

Wandermeter ranking and last review.

Number of Pages Required

1 page

Font styles to use
Serif

Requirements
Must have
• Reservation module
• Marketplace to buy wine pairings and gift certificates
• Wandermeter review
• Chatterbay posts
• All info from old site

```html
<!DOCTYPE html>
<html lang="en">
<head>
<meta charset="utf-8">
<title>Vinosa Bistro – Italian Restaurant</title>
<link rel="stylesheet" href="https://fonts.googleapis.com/css2?family=Cinzel:wght@400;700&family=Open+Sans:wght@400;600;700&display=swap">
<style>
:root{
  --wine:#8d1b22;
  --wine-dark:#6a1218;
  --ink:#1b1b1b;
  --text:#555;
  --paper:#ffffff;
  --mist:#f1f1f1;
  --night:#141213;
  --line:#d9d9d9;
}
*{box-sizing:border-box;margin:0;padding:0}
html,body{width:1200px;height:4848px;overflow:hidden}
body{position:relative;background:var(--paper);font-family:"Open Sans",Arial,sans-serif;color:var(--text);font-size:13px;line-height:1.6}
.abs{position:absolute}
.btn{display:inline-block;background:var(--wine);color:#fff;font-family:"Open Sans",Arial,sans-serif;font-size:12px;font-weight:600;padding:8px 20px;letter-spacing:.5px}
.section-title{position:absolute;left:0;width:1200px;font-family:"Cinzel",Georgia,serif;font-weight:700;color:var(--ink);font-size:34px;text-align:center;line-height:1.2}
.section-title em{font-style:normal;color:var(--wine)}
.section-title.light{color:#fff}
.rule{width:50px;height:3px;background:var(--wine)}
.rule.center{position:absolute;left:575px}
.photo{position:absolute}

/* header */
.topbar{top:0;left:0;width:1200px;height:40px;background:#fff;border-bottom:1px solid var(--line)}
.social{left:150px;top:10px;display:flex;gap:8px}
.social span{width:20px;height:20px;border-radius:50%;background:var(--wine);display:block}
.phone{left:520px;top:9px;font-size:14px;font-weight:600;color:var(--ink);display:flex;align-items:center;gap:8px}
.topbar .cta{top:0;height:40px;padding:0 22px;line-height:40px;background:var(--wine);color:#fff;font-size:12px;font-weight:700;letter-spacing:.5px}
.navbar{top:40px;left:0;width:1200px;height:140px;background:#fff}
.logo{left:80px;top:30px;display:flex;align-items:center;gap:12px}
.logo .mark{width:40px;height:40px;border-radius:50%;background:var(--wine)}
.logo .name{font-family:"Cinzel",Georgia,serif;font-weight:700;font-size:28px;color:var(--wine);line-height:1}
.menu{left:570px;top:48px;display:flex}
.menu a{font-family:"Cinzel",Georgia,serif;color:var(--ink);font-size:15px;padding:6px 22px;border-left:1px solid var(--line);text-decoration:none}
.menu a:first-child{border-left:none;color:var(--wine);border-bottom:2px solid var(--wine)}

/* hero */
.hero{top:180px;left:0;width:1200px;height:540px;background:linear-gradient(100deg,#0d0a0b 0%,#2a1a18 45%,#5a2a1c 70%,#2a1410 100%)}
.hero-text{left:60px;top:310px;color:#fff;font-family:"Cinzel",Georgia,serif}
.hero-text h1{font-weight:400;font-size:48px;letter-spacing:2px;line-height:1.2}
.hero-text p{font-size:22px;line-height:1.4;margin-top:12px}
.arrow{top:420px;width:36px;height:60px;background:rgba(255,255,255,.15)}

/* welcome */
.welcome-title{left:160px;top:740px;font-family:"Cinzel",Georgia,serif;font-weight:700;color:var(--ink);font-size:30px;line-height:1.2}
.welcome-rule{left:160px;top:786px}
.welcome-copy{left:160px;top:805px;width:560px;font-size:12px}
.welcome-copy p{margin-bottom:10px}

/* reservation */
.reserve{top:1132px;left:0;width:1200px;height:460px;background:linear-gradient(90deg,#1d1412,#3a2620 40%,#2a1c18 70%,#16100f)}
.form-box{left:320px;top:1180px;width:560px;height:320px;background:rgba(10,8,8,.78);border:1px solid rgba(255,255,255,.35);padding:22px 36px}
.form-box h3{font-family:"Cinzel",Georgia,serif;color:#fff;font-size:22px;text-align:center;font-weight:400}
.form-box .rule{margin:6px auto 22px}
.fields{display:grid;grid-template-columns:1fr 1fr;gap:14px 22px}
.field{height:40px;border:1px solid rgba(255,255,255,.5);color:#fff;font-size:12px;padding:0 12px;display:flex;align-items:center;justify-content:space-between}
.submit{display:block;width:150px;margin:24px auto 0;text-align:center;font-size:15px;font-weight:700;letter-spacing:1px}

/* menu items */
.feature-card{left:160px;top:1740px;width:355px;height:330px;background:linear-gradient(160deg,#3a2418,#6b3e22 55%,#2a1a14)}
.feature-card h4{position:absolute;left:0;width:100%;top:170px;text-align:center;font-family:"Cinzel",Georgia,serif;color:#fff;font-size:24px;font-weight:400}
.feature-card p{position:absolute;left:40px;width:275px;top:210px;text-align:center;color:#eee;font-size:11px}
.thumb{left:545px;width:120px;height:100px}
.dish{left:690px;width:330px}
.dish h5{font-family:"Cinzel",Georgia,serif;color:var(--ink);font-size:22px;font-weight:400;line-height:1.2}
.dish p{font-size:11px;margin-top:4px}

/* atmosphere */
.atmos{top:2212px;left:0;width:1200px;height:448px;background:linear-gradient(90deg,#120c0c,#3a2620 35%,#4a2a22 60%,#150d0d)}
.atmos-text{left:0;top:2340px;width:1200px;text-align:center;color:#fff}
.atmos-text h2{font-family:"Cinzel",Georgia,serif;font-weight:400;font-size:40px;letter-spacing:2px;line-height:1.2}
.atmos-text h6{font-size:15px;font-weight:600;margin-top:10px}
.atmos-text p{width:860px;margin:10px auto 0;font-size:12px;color:#ddd}
.atmos-text .btn{margin-top:24px}

/* blog */
.intro{left:160px;width:880px;text-align:center;font-size:12px}
.post{top:2880px;width:280px;height:420px;background:var(--mist);border:1px solid var(--line)}
.post .pic{position:absolute;left:10px;top:10px;width:260px;height:180px}
.post h4{position:absolute;left:20px;top:205px;font-family:"Cinzel",Georgia,serif;font-size:17px;color:var(--ink);font-weight:700}
.post p{position:absolute;left:20px;top:238px;width:240px;font-size:11px}
.post .meta{position:absolute;left:20px;top:370px;width:240px;font-size:11px;display:flex;gap:16px;border-top:1px solid var(--line);padding-top:8px}
.post.active{background:var(--wine);border-color:var(--wine)}
.post.active h4,.post.active p,.post.active .meta{color:#fff}
.post.active .meta{border-top-color:rgba(255,255,255,.4)}
.pin{top:2862px;width:34px;height:34px;border-radius:50%;background:#fff;border:2px solid var(--wine)}
.dots{left:0;top:3312px;width:1200px;display:flex;justify-content:center;gap:8px}
.dots span{width:9px;height:9px;border-radius:50%;background:#888}
.dots span:first-child{background:var(--wine)}

/* customers */
.customers{top:3385px;left:0;width:1200px;height:420px;background:linear-gradient(90deg,#171111,#2e201c 45%,#241815 70%,#100c0c)}
.avatar{top:3495px;width:90px;height:90px;border-radius:50%;border:3px solid #fff;background:linear-gradient(#b58a6a,#5e3e2c)}
.avatar-name{top:3595px;width:130px;text-align:center;font-size:12px;color:#ccc}
.quote{left:160px;top:3660px;width:880px;height:120px;background:rgba(255,255,255,.1);padding:18px 30px;color:#ddd;font-size:12px;text-align:center}

/* wine tours */
.tour{top:3980px;width:420px}
.tour .pic{width:420px;height:330px;border:6px solid #fff;box-shadow:0 0 0 1px var(--line)}
.tour h4{font-family:"Cinzel",Georgia,serif;text-align:center;font-size:24px;color:var(--ink);font-weight:400;margin-top:14px}
.tour p{text-align:center;font-size:11px;margin-top:4px}

/* footer */
.footer{top:4500px;left:0;width:1200px;height:300px;background:var(--night);color:#bbb}
.fcol{top:4530px;color:#bbb}
.fcol h5{font-family:"Cinzel",Georgia,serif;color:#fff;font-size:17px;font-weight:700}
.fcol h5 em{font-style:normal;color:var(--wine)}
.fcol ul{list-style:none;margin-top:16px;font-size:12px}
.fcol li{padding:4px 0 4px 12px;position:relative}
.fcol li:before{content:"";position:absolute;left:0;top:12px;width:4px;height:4px;background:var(--wine)}
.contact-line{display:flex;gap:10px;font-size:12px;margin-top:12px}
.feed-item{display:flex;gap:10px;margin-top:12px;font-size:11px;width:330px}
.feed-item span{flex:0 0 50px;height:50px;background:#3a3a3a}
.bottom{top:4800px;left:0;width:1200px;height:48px;background:var(--wine);color:#fff;font-size:11px}
.follow{left:1010px;top:14px;display:flex;gap:6px}
.follow i{width:20px;height:20px;border-radius:50%;background:#fff;opacity:.85;display:block}
</style>
</head>
<body>

<!-- top bar -->
<div class="abs topbar">
  <div class="abs social"><span></span><span></span><span></span><span></span></div>
  <div class="abs phone">
    <svg width="16" height="16" viewBox="0 0 24 24"><path d="M6.6 10.8a15 15 0 0 0 6.6 6.6l2.2-2.2c.3-.3.7-.4 1-.2 1.1.4 2.3.6 3.6.6.6 0 1 .4 1 1V20c0 .6-.4 1-1 1A17 17 0 0 1 3 4c0-.6.4-1 1-1h3.5c.6 0 1 .4 1 1 0 1.3.2 2.5.6 3.6.1.3 0 .7-.2 1z" fill="#8d1b22"/></svg>
    123-456-7890
  </div>
  <div class="abs cta" style="left:660px">BUY GIFT CERTIFICATES</div>
  <div class="abs cta" style="left:900px;background:var(--wine-dark);width:300px;text-align:center">ONLINE RESERVATION</div>
</div>

<!-- navigation -->
<div class="abs navbar">
  <div class="abs logo"><span class="mark"></span><span class="name">Vinosa Bistro</span></div>
  <nav class="abs menu">
    <a>Home</a><a>About Us</a><a>Menu</a><a>Gallery</a><a>Blog</a><a>Contact Us</a>
  </nav>
</div>

<!-- hero -->
<section class="abs hero" role="img" aria-label="Evening street scene outside the restaurant with a glowing sign and a wine glass"></section>
<div class="abs arrow" style="left:0"></div>
<div class="abs arrow" style="right:0"></div>
<div class="abs hero-text">
  <h1>VINOSA BISTRO</h1>
  <p>ITALIAN RESTAURANT IN<br>PORTO LEVA</p>
</div>

<!-- welcome -->
<h2 class="abs welcome-title">Welcome To Vinosa Bistro</h2>
<div class="abs rule welcome-rule"></div>
<div class="abs welcome-copy">
  <p><strong>Lorem ipsum dolor sit amet, consectetur adipiscing elit, sed diam nonummy nibh euismod tincidunt ut laoreet dolore magna aliquam erat.</strong></p>
  <p>Lorem ipsum dolor sit amet, consectetur adipiscing elit, sed diam nonummy nibh euismod tincidunt ut laoreet dolore magna aliquam erat volutpat. Ut wisi enim ad minim veniam, quis nostrud exerci tation ullamcorper suscipit lobortis nisl ut aliquip ex ea commodo consequat. Duis autem vel eum iriure dolor in hendrerit in vulputate velit esse molestie consequat.</p>
  <p>Vel illum dolore eu feugiat nulla facilisis at vero eros et accumsan et iusto odio dignissim qui blandit praesent luptatum zzril delenit augue duis dolore te feugait nulla facilisi. Nam liber tempor cum soluta nobis eleifend option congue nihil imperdiet doming id quod mazim placerat facer possim assum.</p>
</div>
<span class="abs btn" style="left:160px;top:1040px">Read More</span>
<div class="photo" style="left:730px;top:740px;width:300px;height:230px;background:radial-gradient(circle at 50% 55%,#e8d38a,#c9a64a 40%,#7a2a22 75%,#fff 100%)" role="img" aria-label="Bottles of white and red wine with glasses, cheese and grapes"></div>

<!-- reservation -->
<section class="abs reserve" role="img" aria-label="Friends toasting with wine at a dinner table"></section>
<form class="abs form-box">
  <h3>Book Online Reservation</h3>
  <div class="rule"></div>
  <div class="fields">
    <div class="field">Name*<span>&#9786;</span></div>
    <div class="field">Phone*<span>&#9742;</span></div>
    <div class="field">Email*<span>@</span></div>
    <div class="field">No of Guest*<span>&#8962;</span></div>
    <div class="field">Time*<span>&#9719;</span></div>
    <div class="field">Date*<span>&#9638;</span></div>
  </div>
  <span class="btn submit">SUBMIT</span>
</form>

<!-- menu items -->
<div class="photo" style="left:820px;top:1600px;width:380px;height:640px;background:radial-gradient(ellipse at 60% 40%,rgba(141,27,34,.18),rgba(255,255,255,0) 70%)" role="img" aria-label="Faint pouring glass of red wine"></div>
<h2 class="section-title" style="top:1615px">Our <em>Menu Items</em></h2>
<div class="rule center" style="top:1663px"></div>
<div class="abs feature-card" role="img" aria-label="Bar shelves stocked with premium beer">
  <h4>PREMIUM BEER</h4>
  <p>Lorem ipsum dolor sit amet, consectetur adipiscing elit, sed diam nonummy nibh euismod tincidunt laoreet.</p>
</div>
<div class="photo thumb" style="top:1740px;background:linear-gradient(135deg,#c99a6a,#6b3e22)" role="img" aria-label="Plated dessert"></div>
<div class="photo thumb" style="top:1850px;background:linear-gradient(135deg,#a07050,#3a2014)" role="img" aria-label="Cup of coffee"></div>
<div class="photo thumb" style="top:1960px;background:linear-gradient(135deg,#7a3a2a,#1a1010)" role="img" aria-label="Evening cocktail"></div>
<div class="abs dish" style="top:1735px"><h5>Desserts</h5><p>Lorem ipsum dolor sit amet, consectetur adipiscing elit, sed diam nonummy nibh euismod tincidunt ut laoreet dolore magna aliquam erat volutpat.</p></div>
<div class="abs dish" style="top:1845px"><h5>Coffees</h5><p>Lorem ipsum dolor sit amet, consectetur adipiscing elit, sed diam nonummy nibh euismod tincidunt ut laoreet dolore magna aliquam erat volutpat.</p></div>
<div class="abs dish" style="top:1955px"><h5>Nightcap</h5><p>Lorem ipsum dolor sit amet, consectetur adipiscing elit, sed diam nonummy nibh euismod tincidunt ut laoreet dolore magna aliquam erat volutpat.</p></div>
<span class="abs btn" style="left:545px;top:2100px">View More</span>

<!-- atmosphere -->
<section class="abs atmos" role="img" aria-label="Warmly lit dining room with guests at dinner"></section>
<div class="abs atmos-text">
  <h2>UNFORGETTABLE ATMOSPHERE</h2>
  <h6>Lorem Ipsum Dolor Sit Amet, Consectetur Adipiscing Elit, Sed Diam Nonummy</h6>
  <p>Ut wisi enim ad minim veniam, quis nostrud exerci tation ullamcorper suscipit lobortis nisl ut aliquip ex ea commodo consequat. Duis autem vel eum iriure dolor in hendrerit in vulputate velit esse molestie consequat, vel illum dolore eu feugiat nulla facilisis.</p>
  <span class="btn">ONLINE RESERVATIONS</span>
</div>

<!-- blog -->
<h2 class="section-title" style="top:2705px">Latest <em>Blog Posts</em></h2>
<div class="rule center" style="top:2752px"></div>
<p class="abs intro" style="top:2768px">Lorem ipsum dolor sit amet, consectetuer adipiscing elit, sed diam nonummy nibh euismod tincidunt ut laoreet dolore magna aliquam erat volutpat. Ut wisi enim ad minim veniam, quis nostrud exerci tation ullamcorper.</p>

<article class="abs post active" style="left:160px">
  <div class="pic" style="background:linear-gradient(135deg,#d8a070,#8a4a2a)" role="img" aria-label="Plate of grilled shrimp"></div>
  <h4>LOREM IPSUM DOLOR</h4>
  <p>Lorem ipsum dolor sit amet, consectetuer adipiscing elit, sed diam nonummy nibh euismod tincidunt ut laoreet dolore magna aliquam erat volutpat.</p>
  <div class="meta"><span>&#9679; Dec 1, posted by</span><span>&#9993; 0 Comments</span></div>
</article>
<article class="abs post" style="left:460px">
  <div class="pic" style="background:linear-gradient(135deg,#b8b070,#5a6a2a)" role="img" aria-label="Bowl of pasta with greens"></div>
  <h4>LOREM IPSUM DOLOR</h4>
  <p>Lorem ipsum dolor sit amet, consectetuer adipiscing elit, sed diam nonummy nibh euismod tincidunt ut laoreet dolore magna aliquam erat volutpat.</p>
  <div class="meta"><span>&#9679; Dec 1, posted by</span><span>&#9993; 0 Comments</span></div>
</article>
<article class="abs post" style="left:760px">
  <div class="pic" style="background:linear-gradient(135deg,#e0a050,#a83a20)" role="img" aria-label="Baked lasagna with basil"></div>
  <h4>LOREM IPSUM DOLOR</h4>
  <p>Lorem ipsum dolor sit amet, consectetuer adipiscing elit, sed diam nonummy nibh euismod tincidunt ut laoreet dolore magna aliquam erat volutpat.</p>
  <div class="meta"><span>&#9679; Dec 1, posted by</span><span>&#9993; 0 Comments</span></div>
</article>
<span class="abs pin" style="left:283px"></span>
<span class="abs pin" style="left:583px"></span>
<span class="abs pin" style="left:883px"></span>
<div class="abs dots"><span></span><span></span><span></span><span></span></div>

<!-- customers -->
<section class="abs customers" role="img" aria-label="Dimly lit dinner gathering in the background"></section>
<h2 class="section-title light" style="top:3425px;font-size:32px">Our <em>Happy Customers</em></h2>
<div class="rule center" style="top:3470px"></div>
<div class="abs avatar" style="left:415px" role="img" aria-label="Customer portrait"></div>
<div class="abs avatar" style="left:555px;border-color:var(--wine)" role="img" aria-label="Customer portrait"></div>
<div class="abs avatar" style="left:695px" role="img" aria-label="Customer portrait"></div>
<div class="abs avatar-name" style="left:395px">LOREM IPSUM</div>
<div class="abs avatar-name" style="left:535px">LOREM IPSUM</div>
<div class="abs avatar-name" style="left:675px">LOREM IPSUM</div>
<div class="abs quote">Lorem ipsum dolor sit amet, consectetuer adipiscing elit, sed diam nonummy nibh euismod tincidunt ut laoreet dolore magna aliquam erat volutpat. Ut wisi enim ad minim veniam, quis nostrud exerci tation ullamcorper suscipit lobortis nisl ut aliquip ex ea commodo consequat. Duis autem vel eum iriure dolor in hendrerit in vulputate velit esse molestie consequat, vel illum dolore eu feugiat nulla facilisis at vero eros et accumsan.</div>

<!-- wine tours -->
<div class="photo" style="left:880px;top:3820px;width:320px;height:260px;background:radial-gradient(ellipse at 60% 40%,rgba(141,27,34,.35),rgba(255,255,255,0) 70%)" role="img" aria-label="Splash of red wine from a glass"></div>
<h2 class="section-title" style="top:3845px">Wine <em>Tours</em></h2>
<div class="rule center" style="top:3892px"></div>
<p class="abs intro" style="top:3905px;left:280px;width:640px">Lorem ipsum dolor sit amet, consectetuer adipiscing elit, sed diam nonummy nibh euismod tincidunt ut laoreet dolore magna aliquam erat volutpat ut wisi.</p>
<div class="abs tour" style="left:160px">
  <div class="pic" style="background:linear-gradient(135deg,#c8b89a,#7a5a3a 60%,#4a3a2a)" role="img" aria-label="Guests tasting wine at a table"></div>
  <h4>Wine Tasting Tours</h4>
  <p>Lorem ipsum dolor sit amet, consectetuer adipiscing elit, sed diam nonummy nibh euismod tincidunt ut laoreet dolore magna aliquam erat volutpat.</p>
</div>
<div class="abs tour" style="left:620px">
  <div class="pic" style="background:linear-gradient(135deg,#6a1a1a,#2a1010 60%,#c8a070)" role="img" aria-label="Wine bottle and glass paired with food"></div>
  <h4>Wine Pairing Tours</h4>
  <p>Lorem ipsum dolor sit amet, consectetuer adipiscing elit, sed diam nonummy nibh euismod tincidunt ut laoreet dolore magna aliquam erat volutpat.</p>
</div>

<!-- footer -->
<footer>
  <div class="abs footer"></div>
  <div class="abs fcol" style="left:160px">
    <h5>Quick <em>Links</em></h5>
    <ul><li>Home</li><li>About Us</li><li>Menu</li><li>Gallery</li><li>Blog</li><li>Contact Us</li></ul>
  </div>
  <div class="abs fcol" style="left:370px;width:220px">
    <h5>Contact <em>Us</em></h5>
    <div class="contact-line"><span style="color:var(--wine)">&#9679;</span><span>VINOSA BISTRO<br>Lorem Ipsum St. 24<br>Porto Leva</span></div>
    <div class="contact-line"><span style="color:var(--wine)">&#9742;</span><span>123-456-7890</span></div>
    <div class="contact-line"><span style="color:var(--wine)">&#9993;</span><span>hello@vinosabistro.example</span></div>
  </div>
  <div class="abs fcol" style="left:610px">
    <h5>Chatterbay <em>Feed</em></h5>
    <div class="feed-item"><span></span><p>Lorem ipsum dolor sit amet, consectetuer adipiscing elit, sed diam nonummy nibh euismod.</p></div>
    <div class="feed-item"><span></span><p>Lorem ipsum dolor sit amet, consectetuer adipiscing elit, sed diam nonummy nibh euismod.</p></div>
    <div class="feed-item"><span></span><p>Lorem ipsum dolor sit amet, consectetuer adipiscing elit, sed diam nonummy nibh euismod.</p></div>
  </div>
  <div class="photo" style="left:1000px;top:4540px;width:120px;height:220px;background:linear-gradient(180deg,rgba(141,27,34,.1),rgba(141,27,34,.6))" role="img" aria-label="Glass of red wine"></div>
  <div class="abs bottom">
    <span class="abs" style="left:160px;top:15px">Copyright &copy; 2015 Vinosa Bistro. All Rights Reserved.</span>
    <span class="abs" style="left:930px;top:15px">FOLLOW US</span>
    <span class="abs follow"><i></i><i></i><i></i><i></i></span>
  </div>
</footer>

</body>
</html>
```